Real Estate "For Sale" Sign for construction company

We need a sign that we can use to hang on a post and place on the road when we sell a property. The sign will be simple and will need to mainly feature our logo (files attached), as well as the words "For Sale", and then our phone number "(555) 617 3489". The sign will hang on a post that'll look something like the attached picture.

Target Market(s)

Home buyers

Industry/Entity Type

Real Estate

Font styles to use
Serif
Sans Serif

Colors
0054AA
0677BA
7BADD7
CADEEF
E8F1F8
0094D4
00A9DD
6FCCEA
C7EBF8
E9F6FB

Requirements
Must have
• For Sale & our phone number

```html
<!DOCTYPE html>
<html lang="en">
<head>
<meta charset="UTF-8">
<title>Ridgeline Crest Properties – For Sale Sign</title>
<link rel="stylesheet" href="https://fonts.googleapis.com/css2?family=Montserrat:wght@400;800&family=Roboto+Condensed:wght@700&display=swap">
<style>
  :root {
    --page-bg: #ffffff;
    --navy-deep: #1a1b4f;
    --navy: #1f2a66;
    --ridge-blue: #0f4c7f;
    --ridge-mid: #1d3f78;
    --panel: #f8fbfb;
    --brand-blue: #0677BA;
    --sign-text: #ffffff;
  }
  * { margin: 0; padding: 0; box-sizing: border-box; }
  html, body {
    width: 1200px;
    height: 1199px;
    overflow: hidden;
    background: var(--page-bg);
  }
  .sign {
    position: absolute;
    left: 303px;
    top: 224px;
    width: 586px;
    height: 733px;
    background: var(--navy-deep);
    overflow: hidden;
  }
  .sign__backdrop {
    position: absolute;
    inset: 0;
    width: 100%;
    height: 100%;
  }
  .brand-panel {
    position: absolute;
    left: 16px;
    top: 16px;
    width: 554px;
    height: 200px;
    background: var(--panel);
    border-radius: 100px 8px 130px 0 / 80px 8px 110px 0;
    display: flex;
    align-items: center;
    justify-content: center;
    gap: 12px;
    padding-top: 30px;
  }
  .brand-panel__mark {
    width: 18px;
    height: 18px;
    border-radius: 50%;
    background: var(--brand-blue);
  }
  .brand-panel__name {
    font-family: "Montserrat", sans-serif;
    font-weight: 400;
    font-size: 30px;
    color: var(--brand-blue);
    letter-spacing: 0.2px;
  }
  .headline {
    position: absolute;
    right: 60px;
    font-family: "Montserrat", sans-serif;
    font-weight: 800;
    color: var(--sign-text);
    line-height: 1;
    text-align: right;
  }
  .headline--for {
    top: 322px;
    font-size: 72px;
    letter-spacing: 2px;
  }
  .headline--sale {
    top: 390px;
    font-size: 142px;
    letter-spacing: -1px;
  }
  .phone {
    position: absolute;
    right: 58px;
    top: 586px;
    font-family: "Roboto Condensed", sans-serif;
    font-weight: 700;
    font-size: 66px;
    line-height: 1;
    color: var(--sign-text);
    letter-spacing: 1px;
  }
</style>
</head>
<body>
  <div class="sign">
    <svg class="sign__backdrop" viewBox="0 0 586 733" preserveAspectRatio="none" role="img" aria-label="Layered blue mountain ridges landscape">
      <defs>
        <linearGradient id="ridgeGlow" x1="1" y1="0.3" x2="0" y2="1">
          <stop offset="0" stop-color="#0f4c7f"/>
          <stop offset="0.45" stop-color="#1d3f78"/>
          <stop offset="1" stop-color="#1f2360"/>
        </linearGradient>
      </defs>
      <rect width="586" height="733" fill="#16235a"/>
      <polygon points="0,0 586,0 586,733 0,733" fill="url(#ridgeGlow)" opacity="0.9"/>
      <polygon points="0,0 40,0 586,650 586,733 0,733" fill="#153262" opacity="0.45"/>
      <rect y="680" width="586" height="53" fill="var(--navy-deep)"/>
    </svg>

    <div class="brand-panel">
      <span class="brand-panel__mark"></span>
      <span class="brand-panel__name">Ridgeline Crest Properties</span>
    </div>

    <div class="headline headline--for">FOR</div>
    <div class="headline headline--sale">SALE</div>
    <div class="phone">(555) 617 3489</div>
  </div>
</body>
</html>
```